Lindwerk - We create living space - needs a web/WIX design

The website will be in the German language.
During the contest, I welcome designs with English text.
I will provide the German text to the winner.
We prefer WIX-Design for the future, if possible to make the website WiX-ready;

The text to be used in the webpage:
In the project description I’ve written a text about our company in English and in German – as you asked for. Please use this text in the first step.

QUALITY, EXPERTISE and EXPERIENCE
EVERYTHING UNDER A SINGLE ROOF

We are a real estate company based in Vienna, Austria. Our company's main competences are planning, conception, development, erection, sale/renting and management of properties. "We make best quality for the best price" - with this motto LINDWERK offers living space in high quality in Austria as well as in other countries. Thereby the working area of our property development focusses on both new construction and attic extensions.

QUALITÄT, KOMPETENZ UND ERFAHRUNG
ALLES UNTER EINEM DACH​

LINDWERK ist ein Komplettanbieter für Wohnimmobilien von der Vision, Konzeption, Entwicklung, Planung, Errichtung und Verkauf/Vermietung bis zur Hausverwaltung. „Wir bauen beste Qualität zum besten Preis“, unter diesem Motto bietet LINDWERK qualitativ hochwertigen, lebenswerten und nachhaltig gebauten Wohnraum sowohl in Österreich als auch in anderen Ländern an. Dabei konzentriert sich das Arbeitsfeld unserer Bauträgergesellschaft auf die beiden Kernbereiche Neubau und Dachgeschossausbau.

In the boxes “Must haves”, “Nice to haves”, “Should not haves” I’ve mentioned everything the designers need to know (font, colours etc.). AS I’ve received already some very good designs, there should be everything clear for the designers.

During the contest: homepage is welcome

Target Market(s)

Austria, Germany, Europe, Israel, USA; we would like to reach families, singles, male, female, general population and also investors

Industry/Entity Type

Real Estate Development

Number of Pages Required

5+ page

Font styles to use
Other font styles liked:
• See Upload

Colors

Designer to choose colors to be used in the design.

Requirements
Must have
• Pages called: "Company", "Projects", "Investments", "Partner", "Contact"; Link to projects; subsides (Team, News); enough space for renderings; Our company colours are yellow, grey, white and black (see our logo) - our website should be designed in this colours; Website in friendly and light colours
Nice to have
• Our company font for titles - attached; Eventually other font for the text - better readable; We prefer WIX-Design for the future, if possible to make the website WiX-ready.
• It should be clear, that the font in the attachement should be used; the provided files are pictures of our interior designs and the logo; we expect creativity from the designers, so they should use the best pictures in their opinion.
Should not have
• dark design

```html
<!DOCTYPE html>
<html lang="en">
<head>
<meta charset="utf-8">
<title>Lindwerk – We create living space</title>
<link rel="stylesheet" href="https://fonts.googleapis.com/css2?family=Titillium+Web:wght@400;600;700&family=Open+Sans:wght@400;600;700&display=swap">
<style>
:root{
  --yellow:#f2e100;
  --ink:#1d1d1d;
  --grey-dark:#2a2a2a;
  --grey:#6b6b6b;
  --grey-light:#9a9a9a;
  --line:#e3e3e3;
  --paper:#ffffff;
}
*{box-sizing:border-box;margin:0;padding:0}
html,body{width:1200px;height:3144px;overflow:hidden}
body{background:var(--paper);font-family:"Open Sans",Arial,sans-serif;color:var(--ink);position:relative}
h1,h2,h3,h4,.nav{font-family:"Titillium Web",Arial,sans-serif}

/* hero */
.hero-photo{position:absolute;left:0;top:0;width:1200px;height:680px;
  background:linear-gradient(180deg,#d9d6d1 0%,#ebe8e3 40%,#cfcac2 75%,#8e8a84 100%)}
.hero-arrow{position:absolute;top:360px;width:36px;height:36px}
.header{position:absolute;left:88px;top:24px;width:1024px}
.topbar{height:84px;background:var(--paper);display:flex;align-items:center;padding:0 26px}
.brand{font-family:"Open Sans",Arial,sans-serif;font-size:30px;font-weight:400;letter-spacing:.5px;color:var(--ink)}
.contacts{margin-left:auto;display:flex;gap:34px;font-size:15px;color:var(--ink)}
.contacts span{display:flex;align-items:center;gap:8px}
.nav{height:44px;background:var(--grey-dark);display:flex;align-items:center;padding-left:14px;font-size:14px;font-weight:600;color:#fff;text-transform:uppercase}
.nav a{color:#fff;text-decoration:none;padding:0 17px}
.nav .right{margin-left:auto;display:flex;align-items:center;height:100%;font-size:13px;text-transform:none}
.nav .right a{padding:0 12px}
.nav .cta{background:var(--yellow);color:var(--ink);height:100%;display:flex;align-items:center;padding:0 22px;text-transform:uppercase;font-weight:700}

/* intro */
.intro{position:absolute;left:88px;top:592px;width:1024px;height:256px;background:var(--paper);
  box-shadow:0 4px 18px rgba(0,0,0,.15);border-bottom:6px solid var(--yellow);text-align:center;padding:30px 60px}
.values{display:flex;justify-content:center;gap:44px;font-family:"Titillium Web",sans-serif;font-size:28px;font-weight:700}
.values span{display:flex;align-items:center;gap:10px}
.intro h3{font-size:17px;font-weight:600;margin:8px 0 18px;letter-spacing:.5px}
.intro p{font-size:13px;line-height:21px;color:var(--grey)}

/* section headings */
.sec-title{position:absolute;left:0;width:1200px;text-align:center;font-size:30px;font-weight:700;text-transform:uppercase}
.sec-title:after{content:"";display:block;width:60px;height:4px;background:var(--yellow);margin:10px auto 0}

/* properties */
.props{position:absolute;left:88px;top:984px;width:1024px;display:flex;justify-content:space-between}
.prop{width:312px;height:476px;background:var(--paper);box-shadow:0 2px 10px rgba(0,0,0,.12);position:relative}
.prop .img{height:236px}
.prop .body{padding:18px 20px}
.prop h4{font-size:20px;font-weight:700}
.prop .addr{font-size:14px;margin:2px 0 12px}
.prop p{font-size:12px;line-height:19px;color:var(--grey)}
.prop .btn{position:absolute;left:0;bottom:0;width:100%;height:42px;background:var(--yellow);display:flex;align-items:center;justify-content:center;font-size:15px;font-weight:600}
.side-arrow{position:absolute;top:1196px;width:40px;height:40px}

/* team */
.team{position:absolute;left:0;top:1528px;width:1200px;height:476px;
  background:linear-gradient(120deg,#2c2c2c 0%,#494743 50%,#2a2a2a 100%)}
.team h2{position:absolute;top:54px;width:100%;text-align:center;color:#fff;font-size:30px;font-weight:700}
.team-row{position:absolute;left:88px;top:112px;width:1024px;display:flex;justify-content:space-between}
.member{width:236px;height:328px;background:var(--paper);text-align:center}
.member .img{height:248px;margin:8px 8px 0}
.member h4{font-size:19px;font-weight:700;margin-top:12px}
.member small{font-size:11px;color:var(--grey-light)}

/* news */
.news{position:absolute;left:88px;top:2152px;width:1024px;display:flex;justify-content:space-between}
.post{width:312px}
.post .img{height:228px;border:6px solid #fff;box-shadow:0 2px 8px rgba(0,0,0,.15)}
.post h4{font-size:19px;font-weight:700;margin:16px 0 8px}
.meta{display:flex;align-items:center;gap:14px;font-size:11px;color:var(--grey-light)}
.meta span{display:flex;align-items:center;gap:4px}
.tag{background:var(--grey);color:#fff;padding:2px 10px;font-size:10px}
.post p{font-size:12px;line-height:19px;color:var(--grey);margin:10px 0}
.more{font-size:12px;font-weight:600;display:flex;align-items:center;gap:6px}

/* partner */
.partners{position:absolute;left:88px;top:2708px;width:1024px;display:flex;justify-content:space-between}
.partner{width:312px;height:112px;border:1px solid var(--line);display:flex;align-items:center;justify-content:center}

/* footer */
.footer{position:absolute;left:0;top:2872px;width:1200px;height:232px;background:#222;color:#ddd;padding:40px 88px;display:flex}
.footer .about{width:440px}
.footer .brand{color:#fff;font-size:30px}
.footer .about p{font-size:12px;line-height:19px;color:#aaa;margin:12px 0 18px}
.socials{display:flex;gap:14px}
.socials i{width:22px;height:22px;border-radius:50%;background:#bbb;display:block}
.footer h5{font-family:"Titillium Web",sans-serif;font-size:18px;color:#fff;font-weight:700;margin-bottom:16px}
.cities{margin-left:70px;width:230px}
.cities ul{list-style:none;display:grid;grid-template-columns:1fr 1fr;gap:8px 20px;font-size:13px}
.cities li,.contact li{display:flex;align-items:center;gap:8px}
.contact{margin-left:20px}
.contact ul{list-style:none;font-size:13px;display:grid;gap:10px}
.copy{position:absolute;left:0;top:3104px;width:1200px;height:40px;background:#161616;color:#888;font-size:12px;display:flex;align-items:center;justify-content:center}
</style>
</head>
<body>

<div class="hero-photo" role="img" aria-label="Bright interior rendering of a living and dining room"></div>
<svg class="hero-arrow" style="left:14px" viewBox="0 0 36 36"><path d="M22 8 L12 18 L22 28" stroke="#fff" stroke-width="3" fill="none"/></svg>
<svg class="hero-arrow" style="right:14px" viewBox="0 0 36 36"><path d="M14 8 L24 18 L14 28" stroke="#fff" stroke-width="3" fill="none"/></svg>

<header class="header">
  <div class="topbar">
    <div class="brand">Lindwerk</div>
    <div class="contacts">
      <span><svg width="16" height="16" viewBox="0 0 16 16"><path d="M3 1h3l1 4-2 1a9 9 0 0 0 5 5l1-2 4 1v3a2 2 0 0 1-2 2A13 13 0 0 1 1 3a2 2 0 0 1 2-2z" fill="#1d1d1d"/></svg>+1 555-014-0182</span>
      <span><svg width="18" height="14" viewBox="0 0 18 14"><rect x="1" y="1" width="16" height="12" fill="none" stroke="#1d1d1d" stroke-width="1.6"/><path d="M1 1l8 7 8-7" fill="none" stroke="#1d1d1d" stroke-width="1.6"/></svg>hello@lindwerk-example.com</span>
    </div>
  </div>
  <nav class="nav">
    <a>Home</a><a>Company</a><a>Projects</a><a>Investments</a><a>Partner</a><a>Contact</a>
    <div class="right"><a>Login</a><a>Register</a><span class="cta">Get in touch</span></div>
  </nav>
</header>

<section class="intro">
  <div class="values">
    <span><svg width="26" height="26" viewBox="0 0 26 26"><circle cx="13" cy="13" r="12" fill="var(--yellow)"/><path d="M7 13l4 4 8-8" stroke="#1d1d1d" stroke-width="2.6" fill="none"/></svg>QUALITY</span>
    <span><svg width="26" height="26" viewBox="0 0 26 26"><circle cx="13" cy="13" r="12" fill="var(--yellow)"/><path d="M7 13l4 4 8-8" stroke="#1d1d1d" stroke-width="2.6" fill="none"/></svg>EXPERTISE</span>
    <span><svg width="26" height="26" viewBox="0 0 26 26"><circle cx="13" cy="13" r="12" fill="var(--yellow)"/><path d="M7 13l4 4 8-8" stroke="#1d1d1d" stroke-width="2.6" fill="none"/></svg>EXPERIENCE</span>
  </div>
  <h3>EVERYTHING UNDER A SINGLE ROOF</h3>
  <p>We are a real estate company based in Vienna, Austria. Our company's main competences are planning, conception, development, erection, sale/renting and management of properties. "We make best quality for the best price" - with this motto LINDWERK offers living space in high quality in Austria as well as in other countries. Thereby the working area of our property development focusses on both new construction and attic extensions.</p>
</section>

<h2 class="sec-title" style="top:906px">Latest Properties</h2>
<svg class="side-arrow" style="left:20px" viewBox="0 0 40 40"><path d="M26 8 L12 20 L26 32 Z" fill="#bdbdbd"/></svg>
<svg class="side-arrow" style="right:20px" viewBox="0 0 40 40"><path d="M14 8 L28 20 L14 32 Z" fill="var(--yellow)"/></svg>
<div class="props">
  <article class="prop">
    <div class="img" role="img" aria-label="Rendering of a white multi-storey housing project" style="background:linear-gradient(180deg,#b9cde0,#e4e6e8 60%,#9fa3a5)"></div>
    <div class="body"><h4>Housing project</h4><div class="addr">Lindenallee 12 - 1220 Wien</div>
    <p>The property is centrally located in the 22nd district, with 40 apartments, private balconies and terraces from 45 to 110 m² and bright open living areas.</p></div>
    <div class="btn">View Project Site</div>
  </article>
  <article class="prop">
    <div class="img" role="img" aria-label="Rendering of a modern residential building among trees" style="background:linear-gradient(180deg,#c5d7e6,#dfe3dc 55%,#8f9c83)"></div>
    <div class="body"><h4>Housing project</h4><div class="addr">Ahornweg 7 - 1220 Wien</div>
    <p>A quiet green location with 28 apartments, garden units and rooftop terraces from 50 to 120 m², close to schools, shops and public transport.</p></div>
    <div class="btn">View Project Site</div>
  </article>
  <article class="prop">
    <div class="img" role="img" aria-label="Rendering of a single family house with glass facade" style="background:linear-gradient(180deg,#b7cce0,#e8e8e6 55%,#a3a7a3)"></div>
    <div class="body"><h4>Single Family Project</h4><div class="addr">Birkenplatz 4 - 1160 Wien</div>
    <p>Five detached family homes with private gardens, underground parking and spacious living areas from 130 to 160 m² in a calm residential street.</p></div>
    <div class="btn">View Project Site</div>
  </article>
</div>

<section class="team" role="img" aria-label="Dimmed photo of a modern building as background">
  <h2>Meet Our Team</h2>
  <div class="team-row">
    <div class="member"><div class="img" role="img" aria-label="Portrait photo of team member" style="background:linear-gradient(180deg,#c9b8a8,#8e7463)"></div><h4>Mara Voss</h4><small>Project manager</small></div>
    <div class="member"><div class="img" role="img" aria-label="Portrait photo of team member" style="background:linear-gradient(180deg,#d8d0c6,#9a8b7e)"></div><h4>Lena Hart</h4><small>Sales director</small></div>
    <div class="member"><div class="img" role="img" aria-label="Portrait photo of team member" style="background:linear-gradient(180deg,#b7c2cc,#5f6a74)"></div><h4>Mara Voss</h4><small>Lead architect</small></div>
    <div class="member"><div class="img" role="img" aria-label="Portrait photo of team member" style="background:linear-gradient(180deg,#d2d6da,#6c7680)"></div><h4>Tobias Brandt</h4><small>Managing partner</small></div>
  </div>
</section>

<h2 class="sec-title" style="top:2074px">Latest News</h2>
<div class="news">
  <article class="post">
    <div class="img" role="img" aria-label="Rendering of a new residential building" style="background:linear-gradient(180deg,#cfd8df,#e6e4df 60%,#9ea08f)"></div>
    <h4>The Leader In Real Estate</h4>
    <div class="meta"><span class="tag">News</span><span>August 28, 2017</span><span><svg width="12" height="11" viewBox="0 0 12 11"><path d="M1 1h10v7H5l-3 2V8H1z" fill="none" stroke="#9a9a9a"/></svg>0</span></div>
    <p>Our newest development in Vienna has started. Discover bright apartments with terraces and modern, sustainable building standards.</p>
    <div class="more">Read More <svg width="10" height="10" viewBox="0 0 10 10"><path d="M2 1l5 4-5 4z" fill="#1d1d1d"/></svg></div>
  </article>
  <article class="post">
    <div class="img" role="img" aria-label="Rendering of a bright modern interior" style="background:linear-gradient(180deg,#ecebe8,#d6d2cb 60%,#a9a39a)"></div>
    <h4>The Leader In Real Estate</h4>
    <div class="meta"><span class="tag">News</span><span>August 28, 2017</span><span><svg width="12" height="11" viewBox="0 0 12 11"><path d="M1 1h10v7H5l-3 2V8H1z" fill="none" stroke="#9a9a9a"/></svg>0</span></div>
    <p>Attic extensions bring new living space to the city. Read how we combine historic buildings with contemporary interior design.</p>
    <div class="more">Read More <svg width="10" height="10" viewBox="0 0 10 10"><path d="M2 1l5 4-5 4z" fill="#1d1d1d"/></svg></div>
  </article>
  <article class="post">
    <div class="img" role="img" aria-label="Rendering of a townhouse with garden" style="background:linear-gradient(180deg,#d5dde4,#e5e4de 60%,#a4aa98)"></div>
    <h4>The Leader In Real Estate</h4>
    <div class="meta"><span class="tag">News</span><span>August 28, 2017</span><span><svg width="12" height="11" viewBox="0 0 12 11"><path d="M1 1h10v7H5l-3 2V8H1z" fill="none" stroke="#9a9a9a"/></svg>0</span></div>
    <p>New investment opportunities in Austria and abroad. Learn more about our projects for families, singles and investors.</p>
    <div class="more">Read More <svg width="10" height="10" viewBox="0 0 10 10"><path d="M2 1l5 4-5 4z" fill="#1d1d1d"/></svg></div>
  </article>
</div>

<h2 class="sec-title" style="top:2626px">Partner</h2>
<div class="partners">
  <div class="partner"><svg width="70" height="70" viewBox="0 0 70 70"><rect x="5" y="5" width="60" height="60" fill="#c4302b"/></svg></div>
  <div class="partner"><svg width="70" height="70" viewBox="0 0 70 70"><rect x="5" y="5" width="60" height="60" fill="#333"/></svg></div>
  <div class="partner"><svg width="70" height="70" viewBox="0 0 70 70"><circle cx="35" cy="35" r="30" fill="#2a8fb0"/></svg></div>
</div>

<footer class="footer">
  <div class="about">
    <div class="brand">Lindwerk</div>
    <p>We are a real estate company based in Vienna, Austria. Our company's main competences are planning, conception, development, erection, sale/renting and management of properties.</p>
    <div class="socials"><i></i><i></i><i></i><i></i></div>
  </div>
  <div class="cities">
    <h5>PROPERTY CITIES</h5>
    <ul>
      <li><svg width="12" height="12"><circle cx="6" cy="6" r="5" fill="var(--yellow)"/></svg>Austria</li>
      <li><svg width="12" height="12"><circle cx="6" cy="6" r="5" fill="var(--yellow)"/></svg>Israel</li>
      <li><svg width="12" height="12"><circle cx="6" cy="6" r="5" fill="var(--yellow)"/></svg>Germany</li>
      <li><svg width="12" height="12"><circle cx="6" cy="6" r="5" fill="var(--yellow)"/></svg>USA</li>
      <li><svg width="12" height="12"><circle cx="6" cy="6" r="5" fill="var(--yellow)"/></svg>Europe</li>
    </ul>
  </div>
  <div class="contact">
    <h5>CONTACT US</h5>
    <ul>
      <li><svg width="12" height="16" viewBox="0 0 12 16"><path d="M6 0a6 6 0 0 0-6 6c0 5 6 10 6 10s6-5 6-10a6 6 0 0 0-6-6z" fill="var(--yellow)"/><circle cx="6" cy="6" r="2" fill="#222"/></svg>Kastanienweg 3, 1220 Vienna / Austria</li>
      <li><svg width="14" height="14" viewBox="0 0 16 16"><path d="M3 1h3l1 4-2 1a9 9 0 0 0 5 5l1-2 4 1v3a2 2 0 0 1-2 2A13 13 0 0 1 1 3a2 2 0 0 1 2-2z" fill="var(--yellow)"/></svg>+43 1 555 0199</li>
      <li><svg width="16" height="12" viewBox="0 0 18 14"><rect x="1" y="1" width="16" height="12" fill="var(--yellow)"/><path d="M1 1l8 7 8-7" fill="none" stroke="#222" stroke-width="1.6"/></svg>info@lindwerk.example</li>
    </ul>
  </div>
</footer>
<div class="copy">© 2016 by Lindwerk</div>

</body>
</html>
```